Profesional personal website needs design and business card

I need a business card with my professional name as a logo "Marlo Vitality" for my business. I am a Wellness Coach, consultant and trainer. So it should be professional, wellness oriented and modern.

Target Market(s)

Private clients, governments, corporations. Luxury and high market.

Industry/Entity Type

Health And Wellness

Contact Information for Business Card

Marlo Vitality should be the logo

Colors

Designer to choose colors to be used in the design.

Requirements
Must have
• Marlo Vitality
• Name: Tomás Arribal
• Wellness Coach, Consultant & Trainer.
• Website: www.marlovitality.example
• Phone:
• Spain (+34) 612 480 397
• (USA) +1 (555) 318 2046
Nice to have
• The most important is the design of "Marlo Vitality", as this is going to be my personal brand logo. It should be professional, wellness, high end and actual.
Should not have
• no golds, no baroque style..

```html
<!DOCTYPE html>
<html lang="en">
<head>
<meta charset="UTF-8">
<title>Marlo Vitality — Business Card</title>
<link href="https://fonts.googleapis.com/css2?family=Quicksand:wght@500;600;700&display=swap" rel="stylesheet">
<style>
  :root {
    --stage: #2b2c2e;
    --card: #1c1d1f;
    --card-edge: #242528;
    --pattern-a: #222326;
    --pattern-b: #2a2b2e;
    --brand-grey: #d6d7d9;
    --green: #4fc21a;
    --green-deep: #2f9a10;
    --ink-light: #f2f2f2;
    --rule: #4a4b4e;
  }
  * { margin: 0; padding: 0; box-sizing: border-box; }
  html, body { width: 1200px; height: 1108px; overflow: hidden; }
  body {
    background: var(--stage);
    font-family: "Quicksand", sans-serif;
    position: relative;
  }
  .card {
    position: absolute;
    top: 209px;
    width: 410px;
    height: 690px;
    border-radius: 22px;
    background: var(--card);
    box-shadow: 0 18px 40px rgba(0,0,0,0.45);
    overflow: hidden;
  }
  .card--front { left: 150px; }
  .card--back { left: 640px; }

  .brand {
    position: absolute;
    top: 120px;
    left: 0; right: 0;
    text-align: center;
  }
  .brand__dot {
    display: block;
    width: 74px; height: 74px;
    margin: 0 auto 26px;
    border-radius: 50%;
    background: linear-gradient(160deg, var(--green), var(--green-deep));
  }
  .brand__name {
    font-size: 42px;
    font-weight: 500;
    color: var(--brand-grey);
    letter-spacing: 0.5px;
  }

  .person {
    position: absolute;
    top: 392px;
    left: 0; right: 0;
    text-align: center;
  }
  .person__name {
    font-size: 29px;
    font-weight: 700;
    color: var(--green);
  }
  .person__title {
    margin-top: 6px;
    font-size: 16px;
    font-weight: 600;
    color: var(--ink-light);
  }
  .divider {
    width: 230px;
    height: 1px;
    margin: 24px auto 0;
    background: var(--rule);
  }

  .contact {
    position: absolute;
    top: 500px;
    left: 0; right: 0;
    text-align: center;
    list-style: none;
    font-size: 19px;
    font-weight: 600;
    line-height: 1.35;
    color: var(--ink-light);
  }
  .contact .accent { color: var(--green); }

  .back__pattern {
    position: absolute;
    inset: 0;
    background:
      radial-gradient(circle at 30% 20%, var(--pattern-b), transparent 60%),
      linear-gradient(160deg, var(--pattern-b), var(--pattern-a) 70%);
  }
  .back__mark {
    position: absolute;
    top: 420px;
    left: 0; right: 0;
    text-align: center;
    font-size: 17px;
    font-weight: 700;
    color: var(--green);
  }
</style>
</head>
<body>
  <section class="card card--front">
    <div class="brand">
      <span class="brand__dot"></span>
      <div class="brand__name">Marlo Vitality</div>
    </div>
    <div class="person">
      <div class="person__name">Tomás Arribal</div>
      <div class="person__title">Wellness Coach, Consultant &amp; Trainer</div>
      <div class="divider"></div>
    </div>
    <ul class="contact">
      <li>(+34) 612 480 397 <span class="accent">(SPAIN)</span></li>
      <li>+1 (555) 318 2046 <span class="accent">(USA)</span></li>
      <li>www.<span class="accent">marlovitality</span>.example</li>
    </ul>
  </section>

  <section class="card card--back">
    <div class="back__pattern" role="img" aria-label="Subtle tone-on-tone repeating brand pattern across the card back"></div>
    <div class="back__mark">Marlo Vitality</div>
  </section>
</body>
</html>
```